QN6 (acronym stands for Quenport 6)

We are a sales and marketing start up. We sell bar and beverage dispensing equipment presently and we will add foodservice equipment to our portfolio in the coming year. We like our logo but we will consider different presentations of "QN6"

Industry/Entity Type

Marketing

```html
<!DOCTYPE html>
<html lang="en">
<head>
<meta charset="utf-8">
<title>QN6 Business Card</title>
<link href="https://fonts.googleapis.com/css2?family=Roboto+Condensed:wght@400;700&display=swap" rel="stylesheet">
<style>
  :root {
    --stage: #e9e4dc;
    --card-black: #070707;
    --card-sheen: #1c1c1c;
    --gold: #c9964f;
    --ink-light: #eeeeee;
    --silver: #d8d8d8;
  }
  * { margin: 0; padding: 0; box-sizing: border-box; }
  html, body { width: 1200px; height: 1023px; overflow: hidden; }
  body {
    background: var(--stage);
    font-family: "Roboto Condensed", "Arial Narrow", sans-serif;
    display: flex;
    flex-direction: column;
    align-items: center;
    justify-content: center;
    gap: 60px;
  }
  .business-card {
    position: relative;
    width: 580px;
    height: 332px;
    border-radius: 22px;
    background: linear-gradient(135deg, var(--card-sheen) 0%, var(--card-black) 45%, var(--card-black) 100%);
    box-shadow: 0 10px 26px rgba(0,0,0,0.28);
    overflow: hidden;
  }
  .brand-name {
    position: absolute;
    left: 0;
    width: 290px;
    top: 50%;
    transform: translateY(-50%);
    text-align: center;
    font-size: 78px;
    font-weight: 700;
    color: var(--gold);
    letter-spacing: 2px;
    line-height: 1;
  }
  .card-divider {
    position: absolute;
    left: 290px;
    top: 96px;
    width: 2px;
    height: 140px;
    background: linear-gradient(to bottom, transparent, var(--silver) 50%, transparent);
  }
  .contact-block {
    position: absolute;
    left: 326px;
    top: 104px;
    right: 20px;
  }
  .person-name {
    font-size: 19px;
    font-weight: 700;
    color: var(--gold);
    letter-spacing: 1.5px;
    text-transform: uppercase;
    margin-bottom: 18px;
  }
  .contact-line {
    display: flex;
    align-items: center;
    gap: 10px;
    font-size: 15px;
    color: var(--ink-light);
    letter-spacing: 0.5px;
    text-transform: uppercase;
    margin-bottom: 9px;
    white-space: nowrap;
  }
  .contact-icon { width: 17px; height: 17px; flex: none; }
</style>
</head>
<body>
  <svg width="0" height="0" style="position:absolute">
    <defs>
      <symbol id="icon-phone" viewBox="0 0 20 20">
        <circle cx="10" cy="10" r="10" fill="#c9964f"/>
        <path d="M6 5.5c.6-.6 1.4-.5 1.8.2l.9 1.6c.3.5.2 1-.2 1.4l-.6.5c.5 1.2 1.5 2.2 2.7 2.7l.5-.6c.4-.4.9-.5 1.4-.2l1.6.9c.7.4.8 1.2.2 1.8l-.7.7c-3 .6-8.5-4.9-7.9-7.9z" fill="#070707"/>
      </symbol>
      <symbol id="icon-mail" viewBox="0 0 20 20">
        <circle cx="10" cy="10" r="10" fill="#c9964f"/>
        <rect x="5" y="6.5" width="10" height="7" fill="none" stroke="#070707" stroke-width="1.3"/>
        <path d="M5 6.5l5 4 5-4" fill="none" stroke="#070707" stroke-width="1.3"/>
      </symbol>
      <symbol id="icon-web" viewBox="0 0 20 20">
        <circle cx="10" cy="10" r="10" fill="#c9964f"/>
        <circle cx="10" cy="10" r="5.5" fill="none" stroke="#070707" stroke-width="1.2"/>
        <ellipse cx="10" cy="10" rx="2.3" ry="5.5" fill="none" stroke="#070707" stroke-width="1.1"/>
        <path d="M4.5 10h11" stroke="#070707" stroke-width="1.1"/>
      </symbol>
    </defs>
  </svg>

  <article class="business-card">
    <div class="brand-name">QN6</div>
    <div class="card-divider"></div>
    <div class="contact-block">
      <p class="person-name">Dana Morrow</p>
      <p class="contact-line"><svg class="contact-icon"><use href="#icon-phone"/></svg>1-416-555-0137</p>
      <p class="contact-line"><svg class="contact-icon"><use href="#icon-mail"/></svg>info@qn6.example</p>
      <p class="contact-line"><svg class="contact-icon"><use href="#icon-web"/></svg>www.qn6.example</p>
    </div>
  </article>

  <article class="business-card">
    <div class="brand-name">QN6</div>
    <div class="card-divider"></div>
    <div class="contact-block">
      <p class="person-name">Dana Morrow</p>
      <p class="contact-line"><svg class="contact-icon"><use href="#icon-phone"/></svg>1-416-555-0137</p>
      <p class="contact-line"><svg class="contact-icon"><use href="#icon-mail"/></svg>info@qn6.example</p>
      <p class="contact-line"><svg class="contact-icon"><use href="#icon-web"/></svg>www.qn6.example</p>
    </div>
  </article>
</body>
</html>
```